One page site for a home improvement construction company

Looking for a nice, SEO-friendly, single page site for a local handyman. Here's a good example of a similar site: https://pelvoritbuildersnv.com/

My handyman client has many photos of projects (included), so we'd like a nice photo gallery, along with the usual stuff: google map embed, nice contact form (use Elementor native), maybe a place for a few inspirational quotes.

Important: we don't want to use anything other than Elementor Pro and (maybe) a few free plugins to do your design.

Name of business is “Dorian Welkast Home Improvement”

Target Market(s)

Homeowners in upscale communities

Coding

Coded - Design and coding required

Number of Pages Required

1 page

Font styles to use
Serif
Sans Serif

Requirements
Must have
• Must be Built in Elementor. Needs a photo gallery (project portfolio) section with supplied photos.
Nice to have
• A place for an inspirational quote
Should not have
• The top photo should not be Dorian, it should be about the work.

```html
<!DOCTYPE html>
<html lang="en">
<head>
<meta charset="utf-8">
<title>Dorian Welkast Home Improvement</title>
<link rel="stylesheet" href="https://fonts.googleapis.com/css2?family=Montserrat:wght@400;500;600;700&family=Poppins:wght@300;400;500;600;700&family=Tinos:ital,wght@0,700;1,400&display=swap">
<style>
:root{
  --orange:#fe693c;
  --ink:#1d1d1d;
  --text:#333;
  --light:#f6f6f6;
  --panel:#3d3d3d;
  --footer:#2a2a2a;
  --white:#fff;
  --wood:#a3552c;
  --wood-dark:#6e3519;
  --foliage:#5b6a45;
  --map:#e3e3e3;
}
*{margin:0;padding:0;box-sizing:border-box}
html,body{width:1200px;height:3636px;overflow:hidden}
body{position:relative;background:var(--white);font-family:"Poppins",sans-serif;color:var(--text)}
.abs{position:absolute}
a{color:inherit;text-decoration:none}

/* header */
.site-header{position:absolute;left:0;top:0;width:1200px;height:89px;background:var(--white)}
.brand{position:absolute;left:233px;top:25px;display:flex;align-items:center;gap:10px}
.brand-mark{width:28px;height:28px;border:2px solid #555}
.brand-name{font-family:"Montserrat",sans-serif;font-weight:700;font-size:11px;line-height:14px;color:var(--ink);text-transform:uppercase;white-space:nowrap}
.emergency{position:absolute;right:232px;top:17px;font-size:11.5px;color:var(--ink)}
.emergency span{color:var(--orange)}
.main-nav{position:absolute;right:232px;top:50px;display:flex;font-family:"Montserrat",sans-serif;font-weight:600;font-size:10px;color:var(--ink);text-transform:uppercase}
.main-nav a{padding:0 13px;position:relative}
.main-nav a+a::before{content:"/";position:absolute;left:-3px;color:#bbb;font-weight:400}
.main-nav a:last-child{padding-right:0}
.main-nav .active{color:var(--orange)}

/* hero */
.hero{position:absolute;left:0;top:89px;width:1200px;height:473px;
  background:
    radial-gradient(ellipse 60% 35% at 50% 0%,rgba(70,90,60,.85),transparent 70%),
    linear-gradient(90deg,rgba(90,80,70,.55) 0%,transparent 20%,transparent 80%,rgba(90,80,70,.55) 100%),
    linear-gradient(180deg,#5e6450 0%,#7b6e5c 28%,#9c5a34 52%,#b4683a 72%,#8a4a28 100%);
  clip-path:polygon(0 0,100% 0,100% 59%,100% 84%,0 100%)}
.hero-text{position:absolute;left:0;top:88px;width:1200px;text-align:center;color:var(--white);text-shadow:0 1px 3px rgba(0,0,0,.25)}
.hero h1{font-family:"Montserrat",sans-serif;font-weight:600;font-size:46px;line-height:53px}
.hero h1 em{font-style:normal;color:var(--orange)}
.hero .dial{font-size:19px;margin-top:16px}
.hero .phone{font-family:"Montserrat",sans-serif;font-weight:700;font-size:24px;color:var(--orange);margin-top:8px}
.btn{display:inline-block;font-family:"Montserrat",sans-serif;font-weight:700;font-size:11px;text-transform:uppercase;color:var(--white)}
.hero .btn{position:absolute;top:292px;height:45px;line-height:45px;text-align:center}
.btn-fill{background:var(--orange);left:456px;width:156px}
.btn-line{border:2px solid var(--white);left:626px;width:119px;line-height:41px!important}
.slide-arrow{position:absolute;top:265px;width:43px;height:46px;background:var(--white);display:flex;align-items:center;justify-content:center}

/* about */
.about-frame{position:absolute;left:342px;top:600px;width:235px;height:395px;border:8px solid #f0f0f0}
.about-photo{position:absolute;left:233px;top:631px;width:315px;height:335px;
  background:radial-gradient(ellipse 40% 30% at 50% 30%,#a07a62,transparent 75%),
  linear-gradient(180deg,#5d6e45 0%,#6b7a52 40%,#4a5872 62%,#3b4b6a 100%)}
.section-title{font-family:"Montserrat",sans-serif;font-weight:700;font-size:24px;color:var(--ink);text-transform:uppercase}
.title-rule{width:44px;height:2px;background:var(--orange)}
.about-title{left:610px;top:620px}
.about-rule{left:610px;top:659px}
.about-copy{position:absolute;left:610px;top:682px;width:362px;font-size:10.2px;line-height:18.8px;color:#444}
.about-copy p+p{margin-top:18px}
.contact-line{position:absolute;left:610px;display:flex;align-items:center;gap:12px;font-size:13px;color:var(--ink)}
.contact-line .ico{width:24px;height:24px;border-radius:50%;background:var(--orange);display:flex;align-items:center;justify-content:center}
.about-divider{position:absolute;left:845px;top:888px;width:1px;height:66px;background:#ddd}
.follow{position:absolute;left:868px;top:910px;font-size:12px;font-weight:600;color:var(--ink)}
.social-square{position:absolute;left:942px;top:907px;width:25px;height:25px;background:#3b5a9a}

/* services */
.services{position:absolute;left:0;top:1053px;width:1200px;height:527px;background:var(--orange);clip-path:polygon(0 0,100% 0,100% 87%,0 100%)}
.services .section-title{position:absolute;left:0;top:58px;width:1200px;text-align:center;color:var(--white)}
.services .title-rule{position:absolute;left:578px;top:104px;background:var(--white)}
.service-card{position:absolute;top:150px;width:234px;height:214px;border:1.5px solid rgba(255,255,255,.85);text-align:center;color:var(--white)}
.service-card svg{margin-top:38px}
.service-card h3{font-family:"Montserrat",sans-serif;font-weight:700;font-size:15px;line-height:18px;margin-top:18px}
.slider-dots{position:absolute;top:409px;left:0;width:1200px;display:flex;justify-content:center;gap:7px}
.slider-dots i{width:12px;height:12px;border-radius:50%;border:1.5px solid var(--white)}
.slider-dots i.on{background:var(--white)}

/* outreach */
.outreach{position:absolute;left:0;top:1511px;width:1200px;height:677px;background:var(--light);clip-path:polygon(0 10%,100% 0,100% 100%,0 100%);z-index:-1}
.skyline{position:absolute;left:0;top:1835px;width:1200px;height:353px;
  background:
    linear-gradient(180deg,rgba(246,246,246,1) 0%,rgba(246,246,246,0) 35%),
    linear-gradient(180deg,#dfe4ea 0%,#aab6c4 30%,#6f7d90 55%,#59616b 72%,#3d5a45 88%,#2f5a55 100%)}
.outreach-title{left:0;top:1632px;width:1200px;text-align:center}
.outreach-rule{left:578px;top:1673px}
.avatar{position:absolute;border-radius:50%;background:radial-gradient(circle at 50% 40%,#d8b39a 0%,#a47c66 45%,#4d4640 100%);border:3px solid var(--white);box-shadow:0 2px 6px rgba(0,0,0,.15)}
.avatar-main{position:absolute;left:556px;top:1752px;width:104px;height:104px;border:1.5px solid var(--orange);border-radius:50%;padding:6px}
.avatar-main div{width:100%;height:100%;border-radius:50%;background:radial-gradient(circle at 50% 45%,#efd6c4 0%,#cfe0ec 60%,#9fbfd8 100%)}
.quote-mark{position:absolute;left:462px;top:1700px;font-family:"Tinos",serif;font-weight:700;font-size:190px;color:#e4e4e4;line-height:1}
.quote-text{position:absolute;left:350px;top:1871px;width:510px;text-align:center;font-family:"Tinos",serif;font-style:italic;font-size:15.5px;line-height:25px;color:#333}
.quote-cite{position:absolute;left:0;top:1966px;width:1200px;text-align:center;font-family:"Tinos",serif;font-weight:700;font-size:12px;color:var(--ink)}
.quote-cite span{color:#999;font-weight:400;margin:0 6px}
.quote-dots{position:absolute;left:0;top:2002px;width:1200px;display:flex;justify-content:center;gap:7px;align-items:center}
.quote-dots i{width:5px;height:5px;border-radius:50%;background:#999}
.quote-dots i.on{width:8px;height:8px;background:transparent;border:1.5px solid var(--orange)}

/* portfolio */
.portfolio-title{left:0;top:2243px;width:1200px;text-align:center}
.filters{position:absolute;left:0;top:2313px;width:1200px;display:flex;justify-content:center;gap:28px;font-family:"Montserrat",sans-serif;font-weight:600;font-size:9px;color:var(--ink);align-items:center}
.filters .on{color:var(--orange);border:1px solid var(--orange);padding:3px 14px;transform:skewX(-15deg)}
.filters .on span{display:inline-block;transform:skewX(15deg)}
.tile{position:absolute;width:169px;height:157px}
.tile-featured{background:var(--orange);display:flex;align-items:center;justify-content:center}
.tile-featured::after{content:"";position:absolute;inset:12px;border:1px solid rgba(255,255,255,.7)}
.tile-featured span{font-family:"Montserrat",sans-serif;font-weight:700;font-size:12px;color:var(--white)}
.t-siding{background:linear-gradient(180deg,#cfd7de 0%,#8a6a52 30%,#8c8266 60%,#4f5e3c 100%)}
.t-deck{background:linear-gradient(180deg,#6a4a3a 0%,#7b5a46 30%,#c27a4c 55%,#b5693c 80%,#6a5a4a 100%)}
.t-steps{background:linear-gradient(180deg,#9aa0a6 0%,#c58a56 35%,#b06a36 65%,#8a5028 100%)}
.t-pool{background:linear-gradient(160deg,#1f82d0 0%,#3a9de6 55%,#6a6a60 85%,#7a6a58 100%)}
.t-patio{background:linear-gradient(180deg,#dfe5ea 0%,#b5a48c 35%,#6e6a5c 60%,#4f6a34 100%)}
.t-lights{background:linear-gradient(180deg,#5a4a3c 0%,#7a5a40 35%,#b8643a 65%,#8a4424 100%)}
.t-fence{background:linear-gradient(180deg,#7a4a30 0%,#8a4a2a 40%,#a3502a 70%,#6e3519 100%)}

/* contact */
.contact-left{position:absolute;left:0;top:2764px;width:579px;height:494px;background:linear-gradient(135deg,#fb6d42,#f2683e 55%,#ea6238)}
.contact-right{position:absolute;left:579px;top:2764px;width:621px;height:494px;background:var(--panel)}
.tab{position:absolute;left:546px;top:2864px;width:34px;height:320px}
.tab-label{position:absolute;left:546px;top:3024px;width:34px;font-family:"Montserrat",sans-serif;font-weight:700;font-size:21px;color:var(--white);transform:rotate(-90deg);white-space:nowrap;display:flex;justify-content:center}
.contact-title{left:233px;top:2818px;color:var(--white)}
.contact-rule{left:233px;top:2860px;background:var(--white)}
.info-row{position:absolute;left:230px;display:flex;gap:20px;color:var(--white);font-size:16px;line-height:28px}
.info-row .ring{width:38px;height:38px;border-radius:50%;background:var(--white);display:flex;align-items:center;justify-content:center;flex:none}
.info-phone{font-family:"Montserrat",sans-serif;font-weight:600;font-size:20px}
.contact-follow{position:absolute;left:233px;top:3120px;font-family:"Montserrat",sans-serif;font-weight:700;font-size:18px;color:var(--white)}
.social-dot{position:absolute;top:3163px;width:38px;height:38px;border-radius:50%;background:#2b2b2b}
.field{position:absolute;left:610px;width:358px;height:32px;background:var(--white);font-size:9.5px;color:#444;padding:10px 12px}
.field-area{height:92px}
.btn-submit{position:absolute;left:610px;top:3158px;width:120px;height:32px;background:var(--orange);color:var(--white);font-family:"Montserrat",sans-serif;font-weight:700;font-size:11px;text-align:center;line-height:32px}

/* map & footer */
.map{position:absolute;left:0;top:3258px;width:1200px;height:311px;
  background:radial-gradient(ellipse 30% 60% at 72% 55%,#cdcdcd,transparent 70%),
  linear-gradient(90deg,#e6e6e6 0%,#dedede 50%,#d6d6d6 75%,#e2e2e2 100%)}
.map-pin{position:absolute;left:758px;top:3368px}
.site-footer{position:absolute;left:0;top:3569px;width:1200px;height:67px;background:var(--footer);color:#ddd;font-size:10px;text-align:center;line-height:67px}
</style>
</head>
<body>

<header class="site-header">
  <a class="brand" href="https://pelvoritbuildersnv.com/"><span class="brand-mark"></span><span class="brand-name">Dorian Welkast<br>Home Improvement</span></a>
  <p class="emergency">24/7 Emergency Service. <span>Call (800) 5550-1924</span></p>
  <nav class="main-nav">
    <a class="active" href="#">Home</a><a href="#">About</a><a href="#">Services</a><a href="#">Outreach</a><a href="#">Portfolio</a><a href="#">Contact</a>
  </nav>
</header>

<section class="hero" role="img" aria-label="Photo of a finished cedar deck with railings and wooden fence">
  <div class="hero-text">
    <h1>We Are <em>Always</em><br>Ready to Services</h1>
    <p class="dial">For Immediate Services Dial</p>
    <p class="phone">925.555.0148</p>
  </div>
  <a class="btn btn-fill" href="#">View Portfolio</a>
  <a class="btn btn-line" href="#">Contact Us</a>
</section>
<div class="slide-arrow" style="left:0"><svg width="12" height="14" viewBox="0 0 12 14"><path d="M8 1 2 7l6 6" fill="none" stroke="#222" stroke-width="2"/></svg></div>
<div class="slide-arrow" style="right:0"><svg width="12" height="14" viewBox="0 0 12 14"><path d="m4 1 6 6-6 6" fill="none" stroke="#222" stroke-width="2"/></svg></div>

<section class="about">
  <div class="about-frame"></div>
  <div class="about-photo" role="img" aria-label="Portrait photo of Dorian outdoors"></div>
  <h2 class="section-title abs about-title">About</h2>
  <div class="title-rule abs about-rule"></div>
  <div class="about-copy">
    <p>Lorem ipsum dolor sit amet, consectetur adipiscing elit. Suspendisse luctus vulputate metus. Aliquam erat volutpat. Vivamus purus mauris, pretium in pharetra id, sagittis in odio. Aliquam volutpat nulla vitae metus sagittis, vel commodo augue luctus. Proin malesuada turpis lorem, vel dignissim urna euismod vitae. Sed feugiat eleifend lectus, vitae tristique magna imperdiet vel.</p>
    <p>Duis luctus tortor ut velit elementum, ac pretium felis placerat. Interdum et malesuada fames ac ante ipsum primis in faucibus. Quisque eu ex vitae odio fermentum fermentum.</p>
  </div>
  <div class="contact-line" style="top:891px"><span class="ico"><svg width="12" height="12" viewBox="0 0 24 24"><path d="M6.6 10.8a15 15 0 0 0 6.6 6.6l2.2-2.2a1 1 0 0 1 1-.25 11 11 0 0 0 3.6.6 1 1 0 0 1 1 1V20a1 1 0 0 1-1 1A17 17 0 0 1 3 4a1 1 0 0 1 1-1h3.5a1 1 0 0 1 1 1 11 11 0 0 0 .6 3.6 1 1 0 0 1-.25 1z" fill="#fff"/></svg></span><b style="font-weight:600">925.555.0148</b></div>
  <div class="contact-line" style="top:928px"><span class="ico"><svg width="12" height="10" viewBox="0 0 24 18"><path d="M1 1h22v16H1z" fill="#fff"/><path d="m1 1 11 9 11-9" fill="none" stroke="#fe693c" stroke-width="2"/></svg></span>dorianwelkast@mailhub.net</div>
  <div class="about-divider"></div>
  <p class="follow">Follow Us:</p>
  <div class="social-square" role="img" aria-label="Social profile link"></div>
</section>

<section class="services">
  <h2 class="section-title">Our Services</h2>
  <div class="title-rule"></div>
  <div class="service-card" style="left:233px">
    <svg width="72" height="76" viewBox="0 0 72 76" fill="none" stroke="#fff" stroke-width="3"><path d="M8 34h56v14a16 16 0 0 1-16 16H24A16 16 0 0 1 8 48z"/><path d="M24 64l-4 8M48 64l4 8"/><rect x="40" y="10" width="22" height="40" rx="4"/><path d="M14 34V14a8 8 0 0 1 16 0"/><circle cx="22" cy="46" r="3"/></svg>
    <h3>Bathroom<br>Conversions</h3>
  </div>
  <div class="service-card" style="left:484px">
    <svg width="80" height="76" viewBox="0 0 80 76" fill="none" stroke="#fff" stroke-width="3"><path d="M2 14h76v48H2z"/><path d="M2 30h12v16H2M78 30H52v16h26M30 14v10M30 62V52"/></svg>
    <h3>Interior Design<br>Options</h3>
  </div>
  <div class="service-card" style="left:734px">
    <svg width="72" height="76" viewBox="0 0 72 76" fill="none" stroke="#fff" stroke-width="3"><path d="M4 34h64v38H4zM4 52h64"/><path d="M30 43h12M30 61h12"/><path d="M36 34V10a6 6 0 0 1 12 0v4"/><path d="M26 34v-6h20v6"/></svg>
    <h3>Kitchen<br>Remodels</h3>
  </div>
  <div class="slider-dots"><i class="on"></i><i></i><i></i></div>
</section>

<section class="outreach-block">
  <div class="outreach"></div>
  <div class="skyline" role="img" aria-label="Photo of a city skyline at dusk above a river"></div>
  <h2 class="section-title abs outreach-title">Project Outreach</h2>
  <div class="title-rule abs outreach-rule"></div>
  <div class="avatar" role="img" aria-label="Client photo" style="left:257px;top:1653px;width:44px;height:44px"></div>
  <div class="avatar" role="img" aria-label="Client photo" style="left:76px;top:1736px;width:44px;height:44px"></div>
  <div class="avatar" role="img" aria-label="Client photo" style="left:246px;top:1846px;width:64px;height:64px"></div>
  <div class="avatar" role="img" aria-label="Client photo" style="left:0;top:1925px;width:102px;height:102px"></div>
  <div class="avatar" role="img" aria-label="Client photo" style="left:857px;top:1721px;width:58px;height:58px"></div>
  <div class="avatar" role="img" aria-label="Client photo" style="left:1118px;top:1674px;width:74px;height:74px"></div>
  <div class="avatar" role="img" aria-label="Client photo" style="left:1115px;top:1853px;width:70px;height:70px"></div>
  <div class="avatar" role="img" aria-label="Client photo" style="left:902px;top:1946px;width:54px;height:54px"></div>
  <div class="quote-mark" aria-hidden="true">&ldquo;</div>
  <div class="avatar-main" role="img" aria-label="Photo of the quoted customer"><div></div></div>
  <p class="quote-text">Praesent ornare, tellus ac finibus aliquet, libero ex malesuada magna, vitae molestie nibh dui at tortor. Phasellus in nisl eget ligula dictum pharetra. Donec libero nunc, aliquam sed faucibus eu, viverra a nulla. Integer.</p>
  <p class="quote-cite">Owen Harlow<span>|</span>Customer</p>
  <div class="quote-dots"><i></i><i class="on"></i><i></i></div>
</section>

<section class="portfolio">
  <h2 class="section-title abs portfolio-title">Portfolio</h2>
  <div class="filters"><span class="on"><span>All</span></span><span>Kitchen</span><span>Bathroom</span><span>Exterior</span><span>Commercial</span><span>Miscellaneous</span></div>
  <div class="tile tile-featured" style="left:233px;top:2363px"><span>BATHROOM</span></div>
  <div class="tile t-siding" role="img" aria-label="Project photo: exterior siding and roof" style="left:421px;top:2363px"></div>
  <div class="tile t-deck" role="img" aria-label="Project photo: new wooden deck" style="left:610px;top:2363px"></div>
  <div class="tile t-steps" role="img" aria-label="Project photo: wooden steps" style="left:798px;top:2363px"></div>
  <div class="tile t-pool" role="img" aria-label="Project photo: pool with deck" style="left:233px;top:2538px"></div>
  <div class="tile t-patio" role="img" aria-label="Project photo: covered patio" style="left:421px;top:2538px"></div>
  <div class="tile t-lights" role="img" aria-label="Project photo: deck with lights" style="left:610px;top:2538px"></div>
  <div class="tile t-fence" role="img" aria-label="Project photo: deck and fence" style="left:798px;top:2538px"></div>
</section>

<section class="contact">
  <div class="contact-left" role="img" aria-label="Faded photo of deck boards under an orange overlay"></div>
  <div class="contact-right"></div>
  <svg class="tab" viewBox="0 0 34 320"><path d="M34 0V320L0 290V30z" fill="#3d3d3d"/></svg>
  <div class="tab-label">GET IN TOUCH</div>
  <h2 class="section-title abs contact-title">Contact Info</h2>
  <div class="title-rule abs contact-rule"></div>
  <div class="info-row" style="top:2904px"><span class="ring"><svg width="16" height="20" viewBox="0 0 16 20"><path d="M8 1a7 7 0 0 1 7 7c0 5-7 11-7 11S1 13 1 8a7 7 0 0 1 7-7z" fill="none" stroke="#fe693c" stroke-width="1.6"/><circle cx="8" cy="8" r="2.5" fill="none" stroke="#fe693c" stroke-width="1.6"/></svg></span><span>41 Larkfield Lane,<br>Newbrook, 50172<br>United States</span></div>
  <div class="info-row" style="top:2994px"><span class="ring"><svg width="18" height="18" viewBox="0 0 24 24"><path d="M6.6 10.8a15 15 0 0 0 6.6 6.6l2.2-2.2a1 1 0 0 1 1-.25 11 11 0 0 0 3.6.6 1 1 0 0 1 1 1V20a1 1 0 0 1-1 1A17 17 0 0 1 3 4a1 1 0 0 1 1-1h3.5a1 1 0 0 1 1 1 11 11 0 0 0 .6 3.6 1 1 0 0 1-.25 1z" fill="none" stroke="#fe693c" stroke-width="1.6"/></svg></span><span class="info-phone" style="line-height:38px">925.555.0148</span></div>
  <div class="info-row" style="top:3056px"><span class="ring"><svg width="18" height="14" viewBox="0 0 24 18"><path d="M1 1h22v16H1z" fill="none" stroke="#fe693c" stroke-width="1.6"/><path d="m1 1 11 9 11-9" fill="none" stroke="#fe693c" stroke-width="1.6"/></svg></span><span style="line-height:38px">dorianwelkast@mailhub.net</span></div>
  <p class="contact-follow">Follow Us:</p>
  <span class="social-dot" role="img" aria-label="Social profile link" style="left:238px"></span>
  <span class="social-dot" role="img" aria-label="Social profile link" style="left:283px"></span>
  <span class="social-dot" role="img" aria-label="Social profile link" style="left:330px"></span>
  <span class="social-dot" role="img" aria-label="Social profile link" style="left:375px"></span>
  <div class="field" style="top:2842px">Name</div>
  <div class="field" style="top:2893px">Email</div>
  <div class="field" style="top:2944px">Phone</div>
  <div class="field" style="top:2994px">Subject</div>
  <div class="field field-area" style="top:3045px">How can we help you?</div>
  <a class="btn-submit" href="#">SUBMIT</a>
</section>

<div class="map" role="img" aria-label="Greyscale street map of the metro area showing the business location"></div>
<svg class="map-pin" width="30" height="40" viewBox="0 0 30 40" aria-hidden="true"><path d="M15 1a14 14 0 0 1 14 14c0 10-14 24-14 24S1 25 1 15A14 14 0 0 1 15 1z" fill="#fe693c"/><circle cx="15" cy="15" r="5.5" fill="#fff"/></svg>
<footer class="site-footer">Copyright &copy; 2020 Dorian Welkast Home Improvement. All rights reserved.</footer>

</body>
</html>
```